New London Job Board - Business Card Required

Dear All,

I own Quintaro Limited, which in turn owns the website:
www.brambletopfield.com

I want all of you wonderful creative people to come up with a slick, and awesome business card design that incorporates the logo on the site, and some colouring and design elements from it.

You have free reign in how you go about doing this, I won't be giving my contact details on this platform, but the winner will be asked to redesign based on my contact details which I will supply at the end.

I need the design to be completed within 5 days. I need the final print copies of the business cards by the 25th November, so unfortunately it's a bit of a rush to get these designs ready.

Any questions, please ask.

Thank you

Thank you all for your hard work and exceptional designs provided. I do have to pick one, so I have a very clear idea of which one this is, however I will wait one further day until the competition closes to be fair to all those have submitted, or are in the process of submitting. I wish you all the best and thank you again for your dedication.

```html
<!DOCTYPE html>
<html lang="en">
<head>
<meta charset="utf-8">
<title>Brambletop Field – Business Card</title>
<link rel="stylesheet" href="https://fonts.googleapis.com/css2?family=Oswald:wght@400;600&display=swap">
<style>
  :root {
    --backdrop: #e8e6e2;
    --card-dark: #1d1d1d;
    --card-gold: #cfa33c;
    --gold-text: #d6a93c;
    --ink: #1a1a1a;
    --shadow: rgba(0,0,0,0.22);
  }
  * { margin: 0; padding: 0; box-sizing: border-box; }
  html, body {
    width: 1200px; height: 873px; overflow: hidden;
    background: var(--backdrop);
    font-family: "Oswald", "Arial Narrow", sans-serif;
  }
  .stage {
    position: relative; width: 1200px; height: 873px;
    display: flex; align-items: center; justify-content: center; gap: 44px;
  }
  .card {
    position: relative; width: 534px; height: 306px;
    border-radius: 3px; box-shadow: 0 10px 28px var(--shadow);
    overflow: hidden;
  }
  .card--front { background: var(--card-dark); color: var(--gold-text); }
  .card--back { background: var(--card-gold); color: var(--ink); display: flex; align-items: center; justify-content: center; }

  .brand {
    display: flex; align-items: center; gap: 10px;
    font-weight: 400; letter-spacing: 2px; text-transform: uppercase;
  }
  .brand__dot { width: 14px; height: 14px; border-radius: 50%; background: currentColor; flex: none; }
  .card--front .brand { position: absolute; top: 34px; right: 34px; font-size: 18px; }
  .card--back .brand { font-size: 30px; letter-spacing: 3px; }
  .card--back .brand__dot { width: 22px; height: 22px; }

  .contact-list {
    position: absolute; left: 34px; top: 34px;
    list-style: none; font-size: 14px; line-height: 24px; letter-spacing: 0.3px;
  }
  .contact-list li { display: flex; align-items: center; gap: 9px; }
  .contact-list svg { width: 12px; height: 12px; flex: none; fill: currentColor; }

  .person { position: absolute; right: 34px; bottom: 34px; text-align: right; }
  .person__name { font-size: 28px; font-weight: 600; letter-spacing: 1px; text-transform: uppercase; line-height: 1.1; }
  .person__role { font-size: 14px; letter-spacing: 0.5px; }
</style>
</head>
<body>
<main class="stage">
  <section class="card card--front" aria-label="Business card front">
    <ul class="contact-list">
      <li><svg viewBox="0 0 12 12"><path d="M2.5 0.5l2 2.5-1.2 1.4a7 7 0 0 0 4.3 4.3L9 7.5l2.5 2-1 2C5 11.5 0.5 7 0.5 1.5z"/></svg>0700 900 4120</li>
      <li><svg viewBox="0 0 12 12"><path d="M0.5 2h11v8h-11z M1 2.5l5 4 5-4" fill="none" stroke="currentColor" stroke-width="1"/></svg>contact@brambletopfield.com</li>
      <li><svg viewBox="0 0 12 12"><circle cx="6" cy="6" r="5.2" fill="none" stroke="currentColor" stroke-width="1"/><path d="M0.8 6h10.4 M6 0.8c-2.5 3-2.5 7.4 0 10.4 M6 0.8c2.5 3 2.5 7.4 0 10.4" fill="none" stroke="currentColor" stroke-width="0.9"/></svg>www.brambletopfield.com</li>
      <li><svg viewBox="0 0 12 12"><path d="M6 0.5a4 4 0 0 1 4 4c0 3-4 7-4 7s-4-4-4-7a4 4 0 0 1 4-4z M6 3a1.5 1.5 0 1 0 0.01 0z"/></svg>17 Elmsworth Row, Mayfair, London, W1X 0ZZ</li>
    </ul>
    <div class="brand"><span class="brand__dot"></span>Brambletop Field</div>
    <div class="person">
      <p class="person__name">Corwin Hale</p>
      <p class="person__role">Managing Director</p>
    </div>
  </section>

  <section class="card card--back" aria-label="Business card back">
    <div class="brand"><span class="brand__dot"></span>Brambletop Field</div>
  </section>
</main>
</body>
</html>
```